Book Cover Design for Educational Assessment Book

We are a publisher based in Singapore. We need a book cover design for an educational assessment book titled "Keystone Tier Advanced Numeracy Drill Compendium". The book is targeted at high school students, hence the design should look professional and not overly fanciful. This book is the first in a series. Subsequent books will have the same design but of different theme colours. Designers need to take note that the design must allow for different theme colours to be used. Please refer to the attached file 'Syllabus' for the mathematical concepts taught in our book.

Target Market(s)

Singapore Keystone Tier Students/ High School Students

Industry/Entity Type

Education

Requirements
Must have
• 1. A Space for Company Logo on top right
• 2. A Space for ISBN number on bottom right (to be provided later)
• 3. Book Highlights:
• a. "The Most Comprehensive Advanced Numeracy Drill Compendium"
• b. "More than 1000 Questions"
• c. "With Step-by-Step Complete Solutions"
• d. "Latest NCA Syllabus - Syllabus 7132"
• e. "Questions Booklet"
Nice to have
• Nice to have a theme colour, so we can allocate different colours to subsquent books in the same series.
• Nice to have appropriate and simple mathematical graphics or formulae.
Should not have
• Cartoons, Photographs, Flamboyant Graphics

```html
<!DOCTYPE html>
<html lang="en">
<head>
<meta charset="utf-8">
<title>Keystone Tier Advanced Numeracy Drill Compendium — Cover</title>
<link rel="stylesheet" href="https://fonts.googleapis.com/css2?family=Montserrat:wght@700;800;900&display=swap">
<style>
  :root {
    --theme: #0b418f;
    --theme-deep: #0a2f6e;
    --theme-bright: #1b5fd0;
    --ink: #b9b1e2;
    --rule: #b9b1e2;
  }
  * { margin: 0; padding: 0; box-sizing: border-box; }
  html, body { width: 922px; height: 1200px; overflow: hidden; background: var(--theme); }
  .cover {
    position: relative;
    width: 922px;
    height: 1200px;
    background: var(--theme);
    overflow: hidden;
    font-family: "Montserrat", sans-serif;
    color: var(--ink);
  }

  /* Reserved areas for publisher logo and ISBN */
  .logo-space,
  .isbn-space {
    position: absolute;
    border: 1px dashed var(--rule);
    opacity: 0.35;
  }
  .logo-space { right: 32px; top: 32px; width: 150px; height: 110px; }
  .isbn-space { right: 32px; bottom: 32px; width: 170px; height: 100px; }

  /* Tilted layout stage: everything inside shares one angle */
  .stage {
    position: absolute;
    left: -189px; top: 100px;
    width: 1300px; height: 1000px;
    transform: rotate(-25deg);
    transform-origin: center center;
  }
  .stage > * { position: absolute; }

  .title-frame {
    left: 320px; top: 150px;
    width: 760px; height: 220px;
    border-top: 2px solid var(--rule);
    border-left: 2px solid var(--rule);
    border-bottom: 2px solid var(--rule);
  }
  .math-artwork {
    left: 400px; top: 352px;
    width: 770px; height: 318px;
    background: linear-gradient(115deg, var(--theme-deep) 0%, var(--theme-bright) 55%, var(--theme) 100%);
    opacity: 0.85;
  }
  .title-block {
    left: 350px; top: 168px;
    text-transform: uppercase;
    line-height: 1;
    white-space: nowrap;
  }
  .title-main { font-weight: 900; font-size: 78px; letter-spacing: 1px; }
  .title-sub  { font-weight: 800; font-size: 32px; margin-top: 6px; letter-spacing: 1px; }
  .title-end  { font-weight: 900; font-size: 54px; margin-top: 4px; letter-spacing: 1px; }

  .rule-top {
    left: 350px; top: 750px;
    width: 1000px; height: 0;
    border-top: 2px solid var(--rule);
  }
  .rule-bottom {
    left: 370px; top: 962px;
    width: 960px; height: 0;
    border-top: 2px solid var(--rule);
  }
  .rule-side {
    left: 370px; top: 750px;
    width: 0; height: 212px;
    border-left: 2px solid var(--rule);
  }
  .highlights {
    left: 398px; top: 768px;
    width: 560px;
    list-style: none;
    text-transform: uppercase;
    font-weight: 800;
    font-size: 21px;
    line-height: 1.22;
  }
  .highlights li {
    position: relative;
    padding-left: 22px;
    margin-bottom: 4px;
  }
  .highlights li::before {
    content: "›";
    position: absolute;
    left: 0; top: -1px;
    font-weight: 700;
  }
</style>
</head>
<body>
  <main class="cover">
    <div class="logo-space" role="region" aria-label="Reserved space for publisher logo"></div>

    <div class="stage">
      <div class="title-frame"></div>
      <div class="math-artwork" role="img" aria-label="Blueprint-style mathematics artwork: curve on a grid, circle, vectors and formulae such as the quadratic formula and P = 2l + 2w"></div>
      <header class="title-block">
        <h1 class="title-main">Keystone Tier</h1>
        <p class="title-sub">Advanced Numeracy</p>
        <p class="title-end">Drill Compendium</p>
      </header>

      <div class="rule-top"></div>
      <div class="rule-side"></div>
      <div class="rule-bottom"></div>

      <ul class="highlights">
        <li>The Most Comprehensive Advanced Numeracy Drill Compendium</li>
        <li>More than 1000 Questions</li>
        <li>With Step-by-Step Complete Solutions</li>
        <li>Latest NCA Syllabus - Syllabus 7132</li>
        <li>Questions Booklet</li>
      </ul>
    </div>

    <div class="isbn-space" role="region" aria-label="Reserved space for ISBN"></div>
  </main>
</body>
</html>
```